Lanternfield Voyages Business Card Design for Home Based Travel Agency

We already have a logo and I would like to see about getting a Business Card Design. The font on the logo can be changed. We are a home based travel agency and sell cruises and tour packages, etc. I would like the following information put into the design Name of Company and Tag Line from the logo. I would also like the email info@lanternfieldvoyages.example Phone 555-238-6140. Website www.lanternfieldvoyages.example. My name Neil Parton Travel Consultant and my wife's Name Mavis Parton. I would like you to use your imagination as nothing is off limites. Impress Me!

Target Market(s)

Baby Boomers

Industry/Entity Type

Travel Agent

Contact Information for Business Card

See above

Font styles to use
Serif
Sans Serif

Colors

Designer to choose colors to be used in the design.

Requirements
Must have
• Play with different fonts and needs to be easily readable, i.e. not too small of print.
Nice to have
• Use your imagination

```html
<!DOCTYPE html>
<html lang="en">
<head>
<meta charset="utf-8">
<title>Lanternfield Voyages – Business Card</title>
<link rel="stylesheet" href="https://fonts.googleapis.com/css2?family=Source+Sans+3:wght@400;600&family=Cormorant+Garamond:wght@600&display=swap">
<style>
  :root {
    --card-blue: #1272c9;
    --card-blue-back: #1878cf;
    --card-blue-shade: #1468b8;
    --band-white: #ffffff;
    --name-yellow: #f7e33a;
    --ink-light: #ffffff;
    --ink-dark: #1c1c1c;
    --accent-orange: #f08a2c;
    --page: #eceae6;
  }
  * { margin: 0; padding: 0; box-sizing: border-box; }
  html, body { width: 1200px; height: 900px; overflow: hidden; background: var(--page); }
  .canvas { position: relative; width: 1200px; height: 900px; font-family: "Source Sans 3", Arial, sans-serif; }

  .card { position: absolute; overflow: hidden; box-shadow: 0 4px 14px rgba(0,0,0,.18); }

  /* Front */
  .card-front { left: 78px; top: 34px; width: 588px; height: 364px; background: var(--card-blue); }
  .front-band { position: absolute; left: 0; top: 28px; width: 100%; height: 113px; background: var(--band-white); }
  .brand-front { position: absolute; left: 60px; top: 34px; display: flex; align-items: center; gap: 10px; }
  .brand-mark { width: 22px; height: 22px; background: var(--accent-orange); }
  .brand-name { font-family: "Cormorant Garamond", Georgia, serif; font-weight: 600; color: var(--ink-dark); font-size: 26px; line-height: 1; }
  .people { position: absolute; right: 37px; top: 178px; text-align: right; }
  .people-names { color: var(--name-yellow); font-weight: 600; font-size: 19px; line-height: 1.1; }
  .people-role { color: var(--ink-light); font-size: 16px; margin-top: 2px; }
  .contacts { position: absolute; left: 34px; top: 268px; list-style: none; }
  .contacts li { display: flex; align-items: center; gap: 9px; color: var(--ink-light); font-size: 16.5px; height: 21px; }
  .contacts svg { width: 11px; height: 11px; flex: none; }

  /* Back */
  .card-back { left: 388px; top: 505px; width: 567px; height: 352px; background: var(--card-blue-back); }
  .back-blocks { position: absolute; inset: 0; }
  .brand-back { position: absolute; left: 0; right: 0; top: 150px; display: flex; justify-content: center; align-items: center; gap: 12px; }
  .brand-back .brand-mark { width: 28px; height: 28px; }
  .brand-back .brand-name { font-size: 38px; }
</style>
</head>
<body>
<main class="canvas">

  <section class="card card-front" aria-label="Business card front">
    <div class="front-band">
      <div class="brand-front">
        <span class="brand-mark"></span>
        <span class="brand-name">Lanternfield Voyages</span>
      </div>
    </div>
    <div class="people">
      <p class="people-names">Neil Parton | Mavis Parton</p>
      <p class="people-role">Travel Consultant</p>
    </div>
    <ul class="contacts">
      <li>
        <svg viewBox="0 0 12 12" aria-hidden="true"><path fill="#f7e33a" d="M1 4c0-2 2-3 5-3s5 1 5 3l-2 1-1-2H4L3 5zM3 6h6l1 5H2z"/></svg>
        555-238-6140
      </li>
      <li>
        <svg viewBox="0 0 12 12" aria-hidden="true"><rect x="1" y="2.5" width="10" height="7" fill="#f7e33a"/><path d="M1 3l5 4 5-4" stroke="#1272c9" stroke-width="1" fill="none"/></svg>
        info@lanternfieldvoyages.example
      </li>
      <li>
        <svg viewBox="0 0 12 12" aria-hidden="true"><circle cx="6" cy="6" r="5" fill="#f7e33a"/><path d="M3 4c2 0 2 2 4 2s1 3 0 4M6 1c1 2 3 2 4 3" stroke="#1272c9" stroke-width="1" fill="none"/></svg>
        www.lanternfieldvoyages.example
      </li>
    </ul>
  </section>

  <section class="card card-back" aria-label="Business card back">
    <svg class="back-blocks" width="567" height="352" viewBox="0 0 567 352" aria-hidden="true">
      <g fill="var(--card-blue-shade)" opacity=".7">
        <rect x="22" y="0" width="26" height="90"/>
        <rect x="48" y="40" width="22" height="140"/>
        <rect x="0" y="90" width="24" height="160"/>
        <rect x="30" y="190" width="30" height="162"/>
        <rect x="74" y="60" width="36" height="200"/>
        <rect x="92" y="270" width="22" height="82"/>
        <rect x="520" y="0" width="26" height="120"/>
        <rect x="497" y="40" width="22" height="150"/>
        <rect x="545" y="90" width="22" height="170"/>
        <rect x="505" y="200" width="30" height="152"/>
        <rect x="458" y="60" width="34" height="210"/>
        <rect x="452" y="280" width="22" height="72"/>
      </g>
    </svg>
    <div class="brand-back">
      <span class="brand-mark"></span>
      <span class="brand-name">Lanternfield Voyages</span>
    </div>
  </section>

</main>
</body>
</html>
```